Learning platform for primary and secondary schools needs a new design

We need to restyle the website: www.boscolucente.org.
We are developing new functionalities that will enable to turn the platform in an interactive e-learning center for teachers, parents and pupils. Our target is providing contents and learning methods for primary and secondary school.
We want to give a new structure to the homepage and all menu sections and to find a new design that facilitates users to orientate themselves. We love our main picture and we would like to emphasize it. We like our logo and we don't want to change it.
The homepage should fulfil three main tasks:
- welcome visitors;
- encourage visitors to explore three areas of free contents: learning (scopri), experimenting (esperimenti), cooking (ricette)
- convert visitors in logged users (users can register as teachers, parents or students).
We also need a new design for:
- log-in page,
- slideshow,
- galleries of pictures,
- blog page,
- newsletter.
If you have any questions, do not hesitate to contact me.
Good job!
Lucia
Updates
Hi guys,
First of all I'd like to say thanks to all designers that submitted their ideas.
Up to now I didn't find any design that really convinced me, that's why I decided to share with you a design idea that could make easier your job (please see again the project briefing). I can't wait to see your new designs!
Good job
Ciao
Giuliana
Hi guys,
I would like to thank you for all your wonderful design proposals. We have just launched a friends and family voting pool to help us in getting the final decision. We'll let you know the result as soon as possible within tomorrow.
Ciao
Giuliana
Target Market(s)
Italian teachers, parents and students attending primary and secondary school
Industry/Entity Type
Cooking
Look and feel
Each slider illustrates characteristics of the customer's brand and the style your logo design should communicate.

```html
<!DOCTYPE html>
<html lang="it">
<head>
<meta charset="utf-8">
<title>BoscoLucente – il gusto della conoscenza</title>
<link rel="stylesheet" href="https://fonts.googleapis.com/css2?family=Arvo:ital,wght@0,400;0,700;1,400;1,700&family=Lato:wght@400;700&display=swap">
<style>
:root{
  --sky-top:#2aa8e6;
  --sky-mid:#6cc6f0;
  --sky-low:#e6f5fc;
  --ground:#b79c98;
  --ground-edge:#6b4a48;
  --orange:#f47f00;
  --orange-deep:#e86f00;
  --brown:#4a2a0e;
  --text:#555555;
  --grey:#8a8a8a;
  --light:#f5f5f5;
  --footer:#f1f1f1;
  --white:#ffffff;
  --red:#d0392b;
}
*{margin:0;padding:0;box-sizing:border-box}
html,body{width:1050px;height:1200px;overflow:hidden;background:var(--white)}
body{position:relative;font-family:'Arvo',Georgia,serif;color:var(--text)}

.hero{position:absolute;left:0;top:0;width:1050px;height:428px;
  background:linear-gradient(180deg,var(--sky-top) 0%,var(--sky-mid) 40%,var(--sky-low) 85%,var(--white) 100%);overflow:hidden}
.hero-ground{position:absolute;left:0;top:330px}
.town{position:absolute;left:155px;top:120px;width:755px;height:275px;border-radius:6px;
  background:linear-gradient(180deg,#f2b26a 0%,#e87b3a 45%,#f1d98b 75%,#9cc9c6 100%)}
.brand{position:absolute;left:160px;top:62px;display:flex;align-items:center;gap:8px}
.brand-dot{width:18px;height:18px;border-radius:50%;background:var(--orange)}
.brand-name{font-family:'Arvo',serif;font-weight:700;font-size:22px;color:var(--orange)}

.utility{position:absolute;right:146px;top:20px;display:flex;align-items:center;gap:10px;
  font-family:'Lato',sans-serif;font-size:10px;color:var(--white)}
.utility .soc{width:18px;height:18px;border-radius:50%;background:#1d6fb8}
.utility .soc.alt{background:#7fb6d6}
.utility .sep{opacity:.8}
.main-nav{position:absolute;left:452px;top:72px;display:flex;gap:22px;
  font-style:italic;font-size:11px;color:var(--white);text-shadow:0 1px 1px rgba(0,0,0,.25)}
.main-nav .active{font-weight:700;font-style:normal}
.main-nav .caret::after{content:" ▾";font-size:8px}

.welcome{position:absolute;left:0;top:428px;width:1050px;height:240px;text-align:center}
.welcome h1{margin-top:40px;font-size:22px;font-weight:700;font-style:italic;color:var(--orange);
  text-shadow:1px 1px 0 #c45f00}
.welcome h2{font-size:15px;font-weight:700;font-style:italic;color:var(--brown);margin-top:-2px}
.welcome p{width:640px;margin:34px auto 0;font-size:11px;line-height:13px;color:var(--text)}

.areas{position:absolute;left:0;top:668px;width:1050px;height:230px;background:var(--light)}
.area{position:absolute;top:55px;width:160px;text-align:center}
.area .art{width:110px;height:110px;margin:0 auto;border-radius:10px;
  background:linear-gradient(180deg,#c9c9c9,#8a8a8a)}
.area .art.round{border-radius:50%;background:radial-gradient(circle,#f7941d 0%,var(--orange) 80%);
  border:3px solid #e9e9e9}
.area h3{margin-top:8px;font-size:16px;font-weight:700;color:var(--grey)}
.area.featured h3{color:var(--orange);font-style:italic}
.area .more{font-size:8px;font-weight:700;color:#444}

.register{position:absolute;left:0;top:898px;width:1050px;height:142px;background:var(--orange);
  text-align:center;color:var(--white)}
.register h2{margin-top:20px;font-size:22px;font-weight:700;text-shadow:1px 1px 1px rgba(0,0,0,.25)}
.register .sub{font-size:14px;margin-top:-4px}
.register .actions{display:flex;justify-content:center;gap:4px;margin-top:6px}
.btn{width:147px;height:29px;line-height:29px;font-size:12px;font-weight:700;border-radius:2px}
.btn.primary{background:var(--white);color:var(--orange)}
.btn.secondary{background:#8c8c8c;color:var(--white)}
.register .note{margin-top:8px;font-size:11px;font-style:italic;font-weight:700}

.site-footer{position:absolute;left:0;top:1040px;width:1050px;height:160px;background:var(--footer);
  font-family:'Lato',sans-serif;font-size:9px;color:#333}
.site-footer h4{font-family:'Arvo',serif;font-size:11px;font-weight:700;color:#333;margin-bottom:8px}
.col{position:absolute;top:42px}
.col li{list-style:none;line-height:14px}
.social-item{display:flex;align-items:center;gap:4px}
.social-item i{width:10px;height:10px;border-radius:50%;background:#1d6fb8;display:inline-block}
.social-item.alt i{background:#aaa}
.social-item.strong{font-weight:700}
.contact{position:absolute;left:550px;top:44px;width:280px;font-size:8.5px;line-height:15px}
.contact .row{display:flex;align-items:center;gap:6px}
.contact svg{flex:none}
.contact .indent{padding-left:11px}
.contact hr{border:0;border-top:1px solid #ddd;margin:16px 0 15px}
</style>
</head>
<body>

<header class="hero">
  <svg class="hero-ground" width="1050" height="100" viewBox="0 0 1050 100" aria-hidden="true">
    <path d="M8 98 Q60 30 525 18 Q990 30 1048 98 Z" fill="var(--ground)" stroke="var(--ground-edge)" stroke-width="2"/>
  </svg>
  <div class="town" role="img" aria-label="Illustrated Italian street of colourful shop houses: greengrocer, bakery, dairy, butcher and fishmonger, with clouds above"></div>

  <div class="brand"><span class="brand-dot"></span><span class="brand-name">BoscoLucente</span></div>

  <div class="utility">
    <span class="soc"></span><span class="soc alt"></span>
    <span class="sep">|</span><span>Login</span>
    <span class="sep">|</span><span>Register</span>
    <span class="sep">|</span><span>Contact Us</span>
    <span class="sep">|</span>
    <svg width="11" height="11" viewBox="0 0 11 11" aria-label="Search"><circle cx="4.5" cy="4.5" r="3.5" fill="none" stroke="#fff" stroke-width="1.5"/><line x1="7" y1="7" x2="10.5" y2="10.5" stroke="#fff" stroke-width="1.5"/></svg>
  </div>

  <nav class="main-nav">
    <span class="active">Home</span>
    <span class="caret">Scopri</span>
    <span class="caret">Esperimenti</span>
    <span class="caret">Ricette</span>
    <span>Blog</span>
    <span>Glossario</span>
    <span class="caret">Il Progetto</span>
  </nav>
</header>

<section class="welcome">
  <h1>Welcome to BoscoLucente,</h1>
  <h2>il gusto della conoscenza.</h2>
  <p>Lorem ipsum dolor sit amet, consectetuer adipiscing elit, sed diam nonummy nibh euismod tincidunt ut laoreet dolore magna aliquam erat volutpat. Ut wisi enim ad minim veniam, quis nostrud exerci tation ullamcorper suscipit lobortis nisl ut aliquip ex ea commodo consequat.<br>Duis autem vel eum iriure dolor in hendrerit in vulputate velit esse molestie consequat, vel illum dolore eu feugiat nulla facilisis at vero eros et accumsan et iusto odio dignissim qui blandit praesent luptatum zzril delenit augue duis dolore te feugait nulla facilisi.</p>
</section>

<section class="areas">
  <div class="area" style="left:186px">
    <div class="art" role="img" aria-label="Stack of grey books"></div>
    <h3>Scopri</h3>
  </div>
  <div class="area featured" style="left:445px">
    <div class="art round" role="img" aria-label="Three test tubes with green, red and blue liquid on an orange disc"></div>
    <h3>Esperimenti</h3>
    <div class="more">Learn more</div>
  </div>
  <div class="area" style="left:700px">
    <div class="art" role="img" aria-label="Grey cooking pot with steaming lid"></div>
    <h3>Ricette</h3>
  </div>
</section>

<section class="register">
  <h2>Get registered</h2>
  <div class="sub">as teachers, parents or students</div>
  <div class="actions">
    <div class="btn primary">Register Now</div>
    <div class="btn secondary">Learn more</div>
  </div>
  <div class="note">Forever free with unlimited number of users</div>
</section>

<footer class="site-footer">
  <div class="col" style="left:250px">
    <h4>Pages</h4>
    <ul><li>Home</li><li>Contact us</li><li>Privacy &amp; Terms</li></ul>
  </div>
  <div class="col" style="left:400px">
    <h4>Find us</h4>
    <ul>
      <li class="social-item strong"><i></i>Fotoblocco</li>
      <li class="social-item alt"><i></i>Piazza+</li>
    </ul>
  </div>
  <div class="contact">
    <div class="row">
      <svg width="7" height="8" viewBox="0 0 7 8"><path d="M1 0.5 L2.6 0.5 L3 2.5 L2 3.2 Q3 5 4.2 5.6 L5 4.6 L6.6 5.2 L6.6 6.8 Q3 7.5 0.5 2 Z" fill="var(--red)"/></svg>
      <span>+39 06 5550 1234 or +39 06 5550 5678</span>
      <span style="color:#bbb">|</span>
      <svg width="9" height="7" viewBox="0 0 9 7"><rect width="9" height="7" fill="var(--red)"/><path d="M0 0 L4.5 4 L9 0" fill="none" stroke="#fff" stroke-width="0.8"/></svg>
      <span>info@boscolucente.com</span>
    </div>
    <div class="row">
      <svg width="7" height="9" viewBox="0 0 7 9"><rect x="0.5" y="0.5" width="6" height="8" fill="none" stroke="var(--red)"/><rect x="2" y="2" width="3" height="1" fill="var(--red)"/><rect x="2" y="4" width="3" height="1" fill="var(--red)"/></svg>
      <span>Sede della società: Via delle Querce, 14 - 00195 Roma</span>
    </div>
    <div class="indent">Indirizzo della redazione: Viale dei Tigli, 42 - 00195 Roma</div>
    <hr>
    <div>© 2014 Boscolucente. All Rights Reserved.</div>
  </div>
</footer>

</body>
</html>
```